Can Design for Fun, Growing Health Food Brand

We are launching a brand new product, electrolyte seltzer drinks. We want the design to be clean/simple and slightly modern while staying true to our brand identity. Must say "Mineral Hydration" as the product descriptor, sub headline is "Carbonated electrolyte beverage with sea moss and real fruit juice". First flavors will be Watermelon Mint and Mango.

Target Market(s)

Women ages 30-50 who are interested in health wellness/trends

Industry/Entity Type

Health & Wellness

Font styles to use
Sans Serif

Requirements
Must have
• Tall, skinny can, current Brightfen Kelp Logo, use aluminum on can as element in design.
Nice to have
• Be fun, clean and modern. Would like to see the label less busy than our gels.
Should not have
• Avoid putting flavor on bottom 1/5 of can. No gradient color changes. Do not want really detailed or realistic fruit image, prefer drawings or similar.

```html
<!DOCTYPE html>
<html lang="en">
<head>
<meta charset="utf-8">
<title>Brightfen Kelp – Mineral Hydration Watermelon Mint</title>
<link href="https://fonts.googleapis.com/css2?family=Montserrat:wght@800&family=Jost:wght@300;400;500&display=swap" rel="stylesheet">
<style>
  :root {
    --backdrop: #eeeeee;
    --alu-light: #f7f7f7;
    --alu-mid: #d9d9db;
    --alu-dark: #b9babd;
    --kelp-green: #1f5e4f;
    --melon-pink: #d97a8a;
    --melon-pink-soft: #e9a3ae;
    --mint-green: #6fa78f;
    --band-text: #ffffff;
  }
  * { margin: 0; padding: 0; box-sizing: border-box; }
  html, body { width: 1200px; height: 800px; overflow: hidden; }
  body {
    background: var(--backdrop);
    display: flex;
    align-items: center;
    justify-content: center;
    font-family: "Jost", sans-serif;
  }
  .can-label {
    position: relative;
    width: 330px;
    height: 720px;
    border-radius: 22px;
    overflow: hidden;
    background: linear-gradient(90deg, var(--alu-dark) 0%, var(--alu-light) 22%, var(--alu-mid) 45%, var(--alu-light) 68%, var(--alu-dark) 100%);
    display: flex;
    flex-direction: column;
    align-items: center;
  }
  .claims-strip {
    margin-top: 26px;
    font-size: 10px;
    font-weight: 500;
    letter-spacing: 0.18em;
    color: var(--kelp-green);
    white-space: nowrap;
  }
  .brand {
    margin-top: 64px;
    display: flex;
    flex-direction: column;
    align-items: center;
    gap: 6px;
  }
  .brand-dot {
    width: 26px; height: 26px;
    border: 2px solid var(--kelp-green);
    border-radius: 50%;
  }
  .brand-name {
    font-size: 17px;
    font-weight: 400;
    color: var(--kelp-green);
    letter-spacing: -0.01em;
  }
  .descriptor {
    margin-top: 34px;
    font-family: "Montserrat", sans-serif;
    font-weight: 800;
    color: var(--kelp-green);
    text-align: center;
    line-height: 1.02;
    font-size: 46px;
    letter-spacing: -0.01em;
  }
  .flavor {
    margin-top: 10px;
    font-size: 14px;
    font-weight: 400;
    letter-spacing: 0.12em;
    color: var(--melon-pink);
  }
  .fruit-art {
    margin-top: 34px;
    width: 200px;
    height: 170px;
    border-radius: 14px;
    background: linear-gradient(135deg, var(--melon-pink-soft) 0%, var(--melon-pink) 55%, var(--mint-green) 100%);
    opacity: 0.85;
  }
  .base-band {
    position: absolute;
    left: 0; right: 0; bottom: 0;
    height: 200px;
    background: var(--melon-pink);
    display: flex;
    flex-direction: column;
    align-items: center;
    color: var(--band-text);
  }
  .base-band svg { position: absolute; top: -18px; left: 0; }
  .subline {
    margin-top: 44px;
    font-size: 14px;
    font-weight: 300;
    line-height: 1.35;
    text-align: center;
  }
  .volume {
    margin-top: 46px;
    font-size: 14px;
    font-weight: 500;
  }
</style>
</head>
<body>
  <main class="can-label">
    <p class="claims-strip">NO ADDED SUGAR &bull; NATURAL SEA MOSS &bull; PLANT BASED</p>
    <div class="brand">
      <span class="brand-dot"></span>
      <span class="brand-name">Brightfen Kelp</span>
    </div>
    <h1 class="descriptor">MINERAL<br>HYDRATION</h1>
    <p class="flavor">— WATERMELON MINT —</p>
    <div class="fruit-art" role="img" aria-label="Line drawing of a watermelon slice with mint leaves and bubbles"></div>
    <section class="base-band">
      <svg width="330" height="20" viewBox="0 0 330 20" aria-hidden="true">
        <path d="M0 20 L0 10 L40 12 L70 4 L110 9 L150 2 L190 8 L230 3 L270 10 L300 5 L330 9 L330 20 Z" fill="var(--melon-pink)"/>
      </svg>
      <p class="subline">Carbonated electrolyte<br>beverage with sea moss<br>and real fruit juice</p>
      <p class="volume">335 ml</p>
    </section>
  </main>
</body>
</html>
```